K.T.L Electrical Services Pty Ltd

Electrical contracting business. I have a base for the design which i like. The contact number needs to be changed to 0491736250 and the O made more solid and level with the rest of the letters. If you have any other ideas of what would make it better I'm happy to see them.

The back side to be written as dot points with the following:
- Residential & Commercial
- Maintenance
- PV & Battery servicing
- EV Chargers

```html
<!DOCTYPE html>
<html lang="en">
<head>
<meta charset="utf-8">
<title>K.T.L Electrical Services – Business Card</title>
<link href="https://fonts.googleapis.com/css2?family=Arimo:wght@400;700&family=Montserrat:wght@500;600;700&display=swap" rel="stylesheet">
<style>
  :root {
    --page: #ffffff;
    --card: #151515;
    --card-deep: #0b0b0a;
    --card-glow: #1e1e1d;
    --teal: #8aaeae;
    --amber: #f9ae1f;
    --white: #ffffff;
  }
  * { box-sizing: border-box; margin: 0; padding: 0; }
  html, body {
    width: 1200px; height: 1000px; overflow: hidden;
    background: var(--page);
  }
  .sheet { position: relative; width: 1200px; height: 1000px; }
  .card {
    position: absolute; left: 197px; width: 806px; height: 460px;
    border-radius: 22px; overflow: hidden;
    font-family: "Arimo", Arial, sans-serif;
  }
  .card--front {
    top: 33px;
    background: radial-gradient(ellipse at 50% 45%, var(--card-glow) 0%, var(--card-deep) 75%);
  }
  .card--back { top: 507px; background: var(--card); }

  .wordmark {
    position: absolute; text-align: right;
  }
  .wordmark__name {
    display: block; text-align: center;
    font-family: "Montserrat", sans-serif; font-weight: 500;
    color: var(--teal); letter-spacing: 6px; line-height: 1;
  }
  .wordmark__trade {
    display: block; font-weight: 700; color: var(--teal);
    letter-spacing: 0.5px; white-space: nowrap; line-height: 1;
  }
  .wordmark__licence {
    display: block; font-weight: 700; color: var(--amber);
    letter-spacing: 2px; line-height: 1;
  }
  .card--front .wordmark { left: 224px; top: 150px; width: 357px; }
  .card--front .wordmark__name { font-size: 104px; }
  .card--front .wordmark__trade { font-size: 24px; margin-top: 15px; }
  .card--front .wordmark__licence { font-size: 24px; margin-top: 8px; }

  .card--back .wordmark { left: 63px; top: 68px; width: 315px; }
  .card--back .wordmark__name { font-size: 88px; }
  .card--back .wordmark__trade { font-size: 21px; margin-top: 16px; }
  .card--back .wordmark__licence { font-size: 21px; margin-top: 6px; }

  .person { position: absolute; left: 468px; top: 66px; color: var(--white); }
  .person__name {
    font-family: "Montserrat", sans-serif; font-weight: 700;
    font-size: 28px; color: var(--amber); letter-spacing: 0.5px; line-height: 1;
  }
  .person__title {
    font-family: "Montserrat", sans-serif; font-weight: 600;
    font-size: 20px; letter-spacing: 2.5px; margin-top: 14px; line-height: 1;
  }
  .contact { list-style: none; margin-top: 18px; }
  .contact__item {
    display: flex; align-items: center; gap: 8px;
    font-size: 20px; line-height: 1; height: 34px;
  }
  .contact__item--phone { font-size: 22px; }
  .contact__icon { width: 15px; height: 15px; flex: none; }

  .services {
    position: absolute; left: 0; top: 272px; width: 806px;
    display: grid; grid-template-columns: 433px 72px 1fr;
    row-gap: 10px; color: var(--white); font-size: 20px; line-height: 20px;
    list-style: none;
  }
  .services__item--left { text-align: right; }
  .services__dot {
    width: 9px; height: 9px; border-radius: 50%; background: var(--amber);
    align-self: center; justify-self: center;
  }
  .swoosh { position: absolute; left: 0; top: 0; width: 806px; height: 460px; }
</style>
</head>
<body>
<main class="sheet">
  <section class="card card--front" aria-label="Card front">
    <div class="wordmark">
      <span class="wordmark__name">K.T.L</span>
      <span class="wordmark__trade">ELECTRICAL SERVICES P / L</span>
      <span class="wordmark__licence">EC 27413</span>
    </div>
  </section>

  <section class="card card--back" aria-label="Card back">
    <svg class="swoosh" viewBox="0 0 806 460" aria-hidden="true">
      <path d="M0,322 C160,304 340,360 520,425 C610,455 720,462 806,405 L806,460 L0,460 Z" fill="var(--amber)"/>
      <path d="M0,356 C170,342 360,392 575,460 L0,460 Z" fill="var(--card)"/>
      <path d="M0,364 C170,350 360,400 550,460 L0,460 Z" fill="var(--teal)"/>
      <path d="M640,460 C720,450 770,440 806,418 L806,460 Z" fill="var(--card)"/>
    </svg>

    <div class="wordmark">
      <span class="wordmark__name">K.T.L</span>
      <span class="wordmark__trade">ELECTRICAL SERVICES P / L</span>
      <span class="wordmark__licence">EC 27413</span>
    </div>

    <div class="person">
      <p class="person__name">NAME SURNAME</p>
      <p class="person__title">TITLE</p>
      <ul class="contact">
        <li class="contact__item contact__item--phone">
          <svg class="contact__icon" viewBox="0 0 16 16"><rect x="4" y="1" width="8" height="14" rx="1.5" fill="none" stroke="var(--amber)" stroke-width="1.8"/><rect x="6" y="11.5" width="4" height="1.4" fill="var(--amber)"/></svg>
          0491736250
        </li>
        <li class="contact__item">
          <svg class="contact__icon" viewBox="0 0 16 16"><path d="M1,8 L15,2 L11,15 L8,10 Z" fill="var(--amber)"/></svg>
          info@webname.com
        </li>
        <li class="contact__item">
          <svg class="contact__icon" viewBox="0 0 16 16"><circle cx="8" cy="8" r="6.5" fill="none" stroke="var(--amber)" stroke-width="1.6"/><ellipse cx="8" cy="8" rx="2.8" ry="6.5" fill="none" stroke="var(--amber)" stroke-width="1.3"/><line x1="1.5" y1="8" x2="14.5" y2="8" stroke="var(--amber)" stroke-width="1.3"/></svg>
          www.websitename.com
        </li>
      </ul>
    </div>

    <ul class="services">
      <li class="services__item services__item--left">Residential &amp; Commercial</li>
      <li class="services__dot" aria-hidden="true"></li>
      <li class="services__item">Maintenance</li>
      <li class="services__item services__item--left">PV &amp; Battery servicing</li>
      <li class="services__dot" aria-hidden="true"></li>
      <li class="services__item">EV Chargers</li>
    </ul>
  </section>
</main>
</body>
</html>
```